A online shop for solid wood need a Stationary design

A new online shop (in Austria and Germany) for solid wood and steel furniture (feldmark-tischwerk) needs a Stationay design (letterhead, business card, envelope etc...). Dining tables, coffee tables, TV furniture and similar furniture will be sold. Everything will be custom made.

```html
<!DOCTYPE html>
<html lang="en">
<head>
<meta charset="utf-8">
<title>Feldmark Tischwerk – Stationery</title>
<link rel="stylesheet" href="https://fonts.googleapis.com/css2?family=Catamaran:wght@400;500;600;700;800&family=Dancing+Script:wght@600&display=swap">
<style>
  :root {
    --bg: #dcdcdc;
    --paper: #efefef;
    --red: #d9171f;
    --ink: #1f1f1f;
    --grey: #858585;
    --window: #9b9b9f;
    --line: #cfcfcf;
  }
  * { box-sizing: border-box; margin: 0; padding: 0; }
  html, body { width: 1200px; height: 792px; overflow: hidden; }
  body {
    background: var(--bg);
    font-family: "Catamaran", sans-serif;
    color: var(--ink);
    position: relative;
  }
  .sheet {
    position: absolute;
    background: var(--paper);
    overflow: hidden;
  }
  .sheet svg.decor { position: absolute; left: 0; top: 0; }
  .red { color: var(--red); }

  /* brand name block */
  .brand {
    position: absolute;
    display: flex;
    flex-direction: column;
    align-items: center;
    color: var(--red);
    font-weight: 800;
    line-height: 1;
  }
  .brand-mark {
    width: var(--mark);
    height: var(--mark);
    background: var(--red);
    margin-bottom: calc(var(--mark) * 0.22);
  }
  .brand-name { font-size: var(--name); letter-spacing: 0.06em; }
  .brand-sub { font-size: var(--sub); letter-spacing: 0.35em; margin-top: calc(var(--sub) * 0.4); }

  /* business card, contact side */
  .card-contact { left: 184px; top: 132px; width: 170px; height: 97px; }
  .card-contact .brand { left: 6px; top: 6px; width: 42px; --mark: 15px; --name: 7px; --sub: 2.4px; }
  .card-name { position: absolute; left: 9px; top: 49px; font-size: 6.5px; font-weight: 500; line-height: 1; }
  .card-role { position: absolute; left: 9px; top: 56px; font-size: 3.6px; color: var(--grey); }
  .card-contacts { position: absolute; left: 9px; top: 71px; list-style: none; font-size: 2.8px; color: var(--grey); line-height: 1.6; }
  .card-contacts li { display: flex; gap: 3px; align-items: center; }
  .card-tagline { position: absolute; left: 113px; top: 7px; width: 52px; font-size: 2.8px; line-height: 1.35; color: var(--grey); }
  .card-tagline b { color: var(--ink); font-weight: 700; }
  .card-tagline b.red { color: var(--red); }
  .card-web { position: absolute; left: 113px; top: 84px; font-size: 2.8px; color: var(--grey); display: flex; align-items: center; gap: 2px; }
  .card-rule { position: absolute; left: 152px; right: 0; top: 86px; height: 0.8px; background: var(--red); }

  /* business card, brand side */
  .card-brand { left: 379px; top: 132px; width: 169px; height: 97px; }
  .card-brand .brand { left: 0; right: 0; top: 26px; --mark: 24px; --name: 11px; --sub: 3.4px; }
  .card-brand-web { position: absolute; left: 0; right: 0; top: 79px; text-align: center; font-size: 4.2px; font-weight: 600; color: var(--red); }

  /* window envelope */
  .envelope-front { left: 184px; top: 255px; width: 365px; height: 182px; }
  .envelope-front .brand { left: 20px; top: 12px; width: 52px; --mark: 22px; --name: 10px; --sub: 3px; }
  .env-title { position: absolute; left: 12px; top: 67px; font-size: 6px; font-weight: 500; }
  .env-text { position: absolute; left: 12px; top: 75px; font-size: 3.8px; line-height: 1.3; color: var(--grey); }
  .env-window { position: absolute; left: 239px; top: 91px; width: 97px; height: 38px; background: var(--window); border-radius: 2px; }
  .env-band { position: absolute; left: 177px; right: 0; bottom: 0; height: 20px; background: var(--red); }

  /* envelope back */
  .envelope-back { left: 184px; top: 468px; width: 365px; height: 182px; }
  .envelope-back .brand { left: 0; right: 0; top: 9px; --mark: 20px; --name: 10px; --sub: 3px; }
  .env-back-band { position: absolute; left: 165px; right: 0; bottom: 0; height: 20px; background: var(--red); }

  /* letterhead */
  .letterhead { left: 595px; top: 131px; width: 367px; height: 519px; }
  .letterhead .brand { left: 13px; top: 24px; width: 92px; --mark: 36px; --name: 17px; --sub: 5.2px; }
  .lh-topbar { position: absolute; left: 194px; right: 0; top: 0; height: 8px; background: var(--red); }
  .lh-tagline { position: absolute; left: 245px; top: 23px; width: 118px; font-size: 7px; font-weight: 700; line-height: 1.2; }
  .lh-contacts { position: absolute; left: 245px; top: 49px; list-style: none; font-size: 6px; color: var(--grey); line-height: 1.25; }
  .lh-contacts li { display: flex; gap: 7px; margin-bottom: 2.6px; }
  .lh-contacts svg { flex: none; margin-top: 1px; }
  .lh-title { position: absolute; left: 15px; top: 133px; font-size: 9.5px; font-weight: 500; }
  .lh-intro { position: absolute; left: 15px; top: 148px; font-size: 6.2px; line-height: 1.25; color: var(--grey); }
  .lh-greeting { position: absolute; left: 15px; top: 179px; font-size: 6.2px; font-weight: 500; }
  .lh-greeting b { color: var(--red); font-weight: 700; margin-left: 2px; }
  .lh-body { position: absolute; left: 15px; top: 198px; width: 338px; font-size: 5.4px; line-height: 6.6px; color: var(--grey); }
  .lh-body p { margin-bottom: 6.6px; }
  .lh-signature { position: absolute; left: 15px; top: 334px; font-family: "Dancing Script", cursive; font-size: 13px; color: var(--red); border-bottom: 0.8px solid var(--red); line-height: 1.1; padding-right: 1px; }
  .lh-closing { position: absolute; left: 15px; top: 357px; font-size: 6.2px; font-weight: 500; }
  .lh-band { position: absolute; left: 0; right: 0; bottom: 0; height: 20px; background: var(--red); }
</style>
</head>
<body>

  <!-- business card: contact side -->
  <section class="sheet card-contact">
    <div class="brand"><span class="brand-mark"></span><span class="brand-name">FELDMARK</span><span class="brand-sub">TISCHWERK</span></div>
    <p class="card-name">LENA <span class="red">VARGA</span></p>
    <p class="card-role">custom table workshop</p>
    <ul class="card-contacts">
      <li><svg width="3" height="3" viewBox="0 0 10 10"><path d="M5 0a3.6 3.6 0 0 0-3.6 3.6C1.4 6.4 5 10 5 10s3.6-3.6 3.6-6.4A3.6 3.6 0 0 0 5 0z" fill="#d9171f"/></svg>your address here, state, zip code 0004</li>
      <li><svg width="3" height="3" viewBox="0 0 10 10"><path d="M2 0l2 2.6-1.2 1.3a6 6 0 0 0 3.3 3.3L7.4 6 10 8l-1.4 1.8C4.4 10 0 5.6.2 1.4z" fill="#d9171f"/></svg>+41 44 512 80 90</li>
      <li><svg width="3" height="3" viewBox="0 0 10 10"><rect y="1.5" width="10" height="7" fill="#d9171f"/></svg>info@feldmarktischwerk</li>
    </ul>
    <p class="card-tagline"><b>A new online shop for</b><br><b class="red">solid wood</b> <b>and</b> <b class="red">steel furniture</b><br>Dining tables, coffee tables,<br>TV furniture<br>Everything will be custom made.</p>
    <p class="card-web"><svg width="3" height="3" viewBox="0 0 10 10"><circle cx="5" cy="5" r="5" fill="#d9171f"/></svg>www.feldmarktischwerk</p>
    <span class="card-rule"></span>
  </section>

  <!-- business card: brand side -->
  <section class="sheet card-brand">
    <div class="brand"><span class="brand-mark"></span><span class="brand-name">FELDMARK</span><span class="brand-sub">TISCHWERK</span></div>
    <p class="card-brand-web">www.feldmarktischwerk</p>
  </section>

  <!-- window envelope -->
  <section class="sheet envelope-front">
    <div class="brand"><span class="brand-mark"></span><span class="brand-name">FELDMARK</span><span class="brand-sub">TISCHWERK</span></div>
    <p class="env-title">CUSTOM TABLE <span class="red">WORKSHOP</span></p>
    <p class="env-text">Dining tables, coffee tables, TV furniture<br>Everything will be custom made.</p>
    <div class="env-window"></div>
    <div class="env-band"></div>
  </section>

  <!-- envelope back -->
  <section class="sheet envelope-back">
    <svg class="decor" width="365" height="182" viewBox="0 0 365 182">
      <path d="M0 0L24 57H341L365 0" fill="none" stroke="var(--line)" stroke-width="0.8"/>
    </svg>
    <div class="brand"><span class="brand-mark"></span><span class="brand-name">FELDMARK</span><span class="brand-sub">TISCHWERK</span></div>
    <div class="env-back-band"></div>
  </section>

  <!-- letterhead -->
  <section class="sheet letterhead">
    <div class="lh-topbar"></div>
    <div class="brand"><span class="brand-mark"></span><span class="brand-name">FELDMARK</span><span class="brand-sub">TISCHWERK</span></div>

    <p class="lh-tagline">A new online shop for <span class="red">solid wood</span><br>and <span class="red">steel furniture</span></p>
    <ul class="lh-contacts">
      <li><svg width="6" height="6" viewBox="0 0 10 10"><path d="M5 0a3.6 3.6 0 0 0-3.6 3.6C1.4 6.4 5 10 5 10s3.6-3.6 3.6-6.4A3.6 3.6 0 0 0 5 0zm0 2.2a1.4 1.4 0 1 1 0 2.8 1.4 1.4 0 0 1 0-2.8z" fill="#d9171f"/></svg><span>your address here, state,<br>zip code 0004</span></li>
      <li><svg width="6" height="6" viewBox="0 0 10 10"><path d="M2 0l2 2.6-1.2 1.3a6 6 0 0 0 3.3 3.3L7.4 6 10 8l-1.4 1.8C4.4 10 0 5.6.2 1.4z" fill="#d9171f"/></svg><span>+41 44 512 80 90</span></li>
      <li><svg width="6" height="6" viewBox="0 0 10 10"><rect y="1.5" width="10" height="7" fill="#d9171f"/><path d="M0 1.8L5 5.6 10 1.8" fill="none" stroke="#efefef" stroke-width="1"/></svg><span>hello@feldmark-tischwerk.ch</span></li>
      <li><svg width="6" height="6" viewBox="0 0 10 10"><circle cx="5" cy="5" r="4.5" fill="none" stroke="#d9171f" stroke-width="1"/><path d="M0.5 5H9.5M5 0.5V9.5M5 0.5C2.5 3 2.5 7 5 9.5M5 0.5C7.5 3 7.5 7 5 9.5" fill="none" stroke="#d9171f" stroke-width="0.8"/></svg><span>www.feldmark-tischwerk.ch</span></li>
    </ul>

    <h1 class="lh-title">CUSTOM TABLE <span class="red">WORKSHOP</span></h1>
    <p class="lh-intro">Dining tables, coffee tables,<br>TV furniture<br>Everything will be custom made.</p>
    <p class="lh-greeting">Dear <b>Lena Varga</b></p>

    <div class="lh-body">
      <p>Thank you for your interest in our furniture. Every piece we make starts with a conversation about the room it will live in, the people who will gather around it and the way it will be used from day to day. From that first talk we choose the timber, plan the proportions and decide how the steel frame should meet the wood. Oak, walnut and ash are dried slowly and sorted by grain before any board is cut. The steel parts are welded, ground and powder coated in our own workshop, so that every joint is clean and every surface is finished by hand. Each table is built once, for one home only.</p>
      <p>Your order will be planned together with you in a short drawing that shows the size, the wood and the frame. Once you approve it, we start building, and we keep you informed at every step until the finished piece is delivered and set up in your home.</p>
      <p>We deliver across Austria and Germany with our own team, who carry the furniture inside, assemble it where it belongs and take all packaging away again. Should anything need adjusting after delivery, we return and take care of it. Solid wood is a living material that changes a little with the seasons, so with each piece you receive a care guide and a small bottle of natural oil for the surface. If you would like to see samples of wood and steel finishes before deciding, we are happy to send a selection to you free of charge. We look forward to building a table that will stay with you for many years and become part of your home.</p>
    </div>

    <p class="lh-signature">Jonas Brenner</p>
    <p class="lh-closing">Sincerely</p>

    <div class="lh-band"></div>
  </section>

</body>
</html>
```